electrical contractor business card for professional modern company

I need a business card design for an electrical contractors business. I do all kinds of electricical work from new homes, air conditioning, data and communications. I have a logo design i want on it and have a good idea in my head of what i want it to look like. I like simple yet bold and professional looking. All black background is a must

Target Market(s)

Anyone needing electrical work done

Industry/Entity Type

Electrical

Contact Information for Business Card

company name- KTW Electrical and Data
person name-martin pellowe
phone number- 0418 362 927
website-ktwelec.example.com.au

Font styles to use
Sans Serif

Requirements
Must have
• email
• website
• logo
• name
• phone number
• list of work i do:
• -electrical
• -air-conditioning
• -data/communications
• -cctv/security
• -domestic/commercial/industrial
• -24hr emergency breakdown repair
Nice to have
• i would like the logo on the front side in the centre taking up most of the card with black background.
• on the rear i want the list of work i do with company info i.e. email, website, my name, phone number. rear of card also black background with orange writing to match the orange in the logo

```html
<!DOCTYPE html>
<html lang="en">
<head>
<meta charset="utf-8">
<title>KTW Electrical and Data – Business Card</title>
<link rel="stylesheet" href="https://fonts.googleapis.com/css2?family=Michroma&family=Ubuntu:wght@400;500&display=swap">
<style>
  :root {
    --stage: #121212;
    --card-black: #050505;
    --panel-dark: #222222;
    --panel-grey-light: #6a6a6a;
    --panel-grey-dark: #3c3c3c;
    --orange: #e8743b;
    --orange-deep: #c9561f;
    --text-light: #e6e6e6;
    --text-muted: #bdbdbd;
  }
  * { box-sizing: border-box; margin: 0; padding: 0; }
  html, body {
    width: 1200px; height: 871px; overflow: hidden;
    background: var(--stage);
  }
  .stage {
    width: 1200px; height: 871px;
    display: flex; flex-direction: column; align-items: center; justify-content: center;
    gap: 48px;
  }
  .card {
    position: relative;
    width: 640px; height: 366px;
    background: var(--card-black);
    overflow: hidden;
    box-shadow: 0 18px 40px rgba(0,0,0,.6);
  }

  /* Services side */
  .card-services .sweep { position: absolute; inset: 0; width: 100%; height: 100%; }
  .service-list {
    position: absolute; left: 34px; top: 38px;
    list-style: none;
    font-family: "Michroma", sans-serif;
    font-size: 11.5px; letter-spacing: 1.6px;
    color: var(--text-light);
    text-transform: uppercase;
  }
  .service-list li { margin-bottom: 29px; }
  .service-list li::before { content: "•"; margin-right: 10px; color: var(--text-muted); }
  .service-list li:last-child { font-size: 13px; }
  .brand-name {
    font-family: "Michroma", sans-serif;
    color: var(--orange);
    font-weight: 400;
    text-transform: uppercase;
    text-align: center;
    line-height: 1.25;
  }
  .card-services .brand-name {
    position: absolute; right: 52px; top: 36px;
    font-size: 16px; letter-spacing: 1px;
  }
  .brand-name .brand-main { display: block; font-size: 2.6em; letter-spacing: 4px; }

  /* Contact side */
  .logo-panel {
    position: absolute; left: 0; top: 0;
    width: 330px; height: 286px;
    background: linear-gradient(135deg, var(--panel-grey-light), var(--panel-grey-dark));
    display: flex; align-items: center; justify-content: center;
  }
  .logo-panel .brand-name { font-size: 13px; letter-spacing: 1px; }
  .base-rule {
    position: absolute; left: 0; right: 0; top: 296px; height: 4px;
    background: linear-gradient(90deg, var(--orange-deep), var(--orange));
  }
  .divider {
    position: absolute; left: 352px; top: 100px; width: 2px; height: 158px;
    background: var(--orange);
  }
  .contact {
    position: absolute; left: 374px; top: 112px;
    font-family: "Ubuntu", sans-serif;
    color: var(--text-light);
  }
  .contact-name {
    font-family: "Michroma", sans-serif;
    color: var(--orange);
    font-size: 15px; letter-spacing: 3px;
    text-transform: uppercase;
    margin-bottom: 12px;
  }
  .contact-line {
    display: flex; align-items: center; gap: 9px;
    font-size: 15px; margin-bottom: 7px;
  }
  .contact-line svg { width: 13px; height: 13px; flex: none; }
</style>
</head>
<body>
<main class="stage">

  <section class="card card-services" aria-label="Card back: services">
    <svg class="sweep" viewBox="0 0 640 366" preserveAspectRatio="none" aria-hidden="true">
      <path d="M0 0 H300 C330 90 390 200 470 300 L640 366 H0 Z" fill="var(--panel-dark)"/>
      <path d="M300 0 H318 C350 90 400 190 470 300 C400 210 340 110 300 0 Z" fill="var(--orange)"/>
    </svg>
    <ul class="service-list">
      <li>Electrical</li>
      <li>Air-conditioning</li>
      <li>Data/communications</li>
      <li>CCTV/security</li>
      <li>Domestic/commercial/industrial</li>
      <li>24hr emergency breakdown repair</li>
    </ul>
    <p class="brand-name"><span class="brand-main">KTW</span>Electrical and Data</p>
  </section>

  <section class="card card-contact" aria-label="Card front: contact details">
    <div class="logo-panel">
      <p class="brand-name"><span class="brand-main">KTW</span>Electrical and Data</p>
    </div>
    <div class="base-rule"></div>
    <div class="divider"></div>
    <div class="contact">
      <p class="contact-name">Martin Pellowe</p>
      <p class="contact-line">
        <svg viewBox="0 0 12 12" aria-hidden="true"><rect x="3" y="0.5" width="6" height="11" rx="1" fill="none" stroke="var(--text-light)"/><circle cx="6" cy="9.6" r="0.7" fill="var(--text-light)"/></svg>
        0418 362 927
      </p>
      <p class="contact-line">
        <svg viewBox="0 0 12 12" aria-hidden="true"><rect x="0.5" y="2.5" width="11" height="7" fill="none" stroke="var(--text-light)"/><path d="M0.5 2.5 L6 6.5 L11.5 2.5" fill="none" stroke="var(--text-light)"/></svg>
        Email@
      </p>
      <p class="contact-line">
        <svg viewBox="0 0 12 12" aria-hidden="true"><circle cx="6" cy="6" r="5.3" fill="none" stroke="var(--text-light)"/><ellipse cx="6" cy="6" rx="2.2" ry="5.3" fill="none" stroke="var(--text-light)"/><path d="M0.7 6 H11.3" stroke="var(--text-light)"/></svg>
        website-ktwelec.example.com.au
      </p>
    </div>
  </section>

</main>
</body>
</html>
```